Harwick Assurance Partners Ltd needs a business card and logo

We need a logo for documents, invoices etc and a business card to match. We are a health auditing, training and consulting company based in NZ and working in both Australia and NZ. We ensure health organisations meet all their compliance requirements and develop expertise in the health auditing sector. The design should in some way reflect either symbols for quality management in the health sector.

Target Market(s)

Health providers and those wishing to increase their capability in meeting and understanding compliance requirements

Industry/Entity Type

Business

Contact Information for Business Card

Logo plus contact details

Logo Text

Health auditing, consultancy and training

Requirements
Must have
• Name and contact details director: Molly Strand, mstrand@hap-example.co.nz, PO Box 318, Kestrel Bay, NZ, cell +6427391065

```html
<!DOCTYPE html>
<html lang="en">
<head>
<meta charset="utf-8">
<title>Harwick Assurance Partners Ltd – Business Card</title>
<link rel="stylesheet" href="https://fonts.googleapis.com/css2?family=Roboto:wght@300;400;700&display=swap">
<style>
  :root {
    --backdrop: #d9d9d9;
    --card: #ffffff;
    --ink-strong: #333333;
    --ink: #3a3a3a;
    --brand-plum: #5a2f4a;
    --brand-green: #4f8a6c;
  }
  * { margin: 0; padding: 0; box-sizing: border-box; }
  html, body {
    width: 1200px;
    height: 1099px;
    overflow: hidden;
    background: var(--backdrop);
    font-family: "Roboto", Arial, sans-serif;
  }
  .canvas {
    position: relative;
    width: 1200px;
    height: 1099px;
  }
  .business-card {
    position: absolute;
    left: 100px;
    top: 230px;
    width: 1000px;
    height: 640px;
    background: var(--card);
  }
  .brand-lockup {
    position: absolute;
    right: 56px;
    top: 84px;
    display: flex;
    align-items: center;
    gap: 28px;
  }
  .brand-name {
    font-weight: 700;
    font-size: 112px;
    line-height: 1;
    letter-spacing: 6px;
    color: var(--brand-plum);
  }
  .brand-dot {
    width: 150px;
    height: 150px;
    display: block;
  }
  .contact-block {
    position: absolute;
    left: 54px;
    top: 306px;
    color: var(--ink);
    font-size: 38px;
    line-height: 49px;
    white-space: nowrap;
  }
  .contact-name { font-weight: 700; color: var(--ink-strong); }
  .contact-company { font-weight: 400; }
  .contact-detail { font-weight: 300; }
</style>
</head>
<body>
<main class="canvas">
  <section class="business-card">
    <div class="brand-lockup">
      <span class="brand-name">HAP</span>
      <svg class="brand-dot" viewBox="0 0 150 150" aria-hidden="true">
        <circle cx="75" cy="75" r="75" fill="var(--brand-green)"/>
      </svg>
    </div>
    <div class="contact-block">
      <p class="contact-name">Molly Strand</p>
      <p class="contact-company">Harwick Assurance Partners Ltd</p>
      <p class="contact-detail">mstrand@hap-example.co.nz</p>
      <p class="contact-detail">+6427391065</p>
      <p class="contact-detail">PO Box 318, Kestrel Bay, Norwick Isle</p>
    </div>
  </section>
</main>
</body>
</html>
```